Lone Prairie Canvas & Sound Jubilee

Organization:
Lone Prairie Canvas and Sound Jubilee is a non-profit organization created by a group of anonymous donors to bring more fun, culture, and art to a small Texas town. Our mission is to promote art and music in Washington County.
The multi-day eclectic festival will feature three stages, a film, art vendors, live mural artists, and food trucks set up throughout historic downtown Brenham. The event is FREE to the public.
Goals:
We need an attractive poster to publicize the festival.
Details:
Lone Prairie Canvas and Sound Jubilee
Friday, October 14 – 16
Free admission (VIP tickets available)
Live music- 3 stages/10 bands
Film Screening
Art vendors and art walk
Live art murals
Food trucks
www.loneprairiecanvasandsoundjubilee.example
#loneprairiecanvasandsound
Requirements:
Please incorporate our festival logo attached.
Conclusion:
After selecting a poster design, we hope to continue to work with the artist to design other event materials including website splash page and rack cards using design elements from the poster.

```html
<!DOCTYPE html>
<html lang="en">
<head>
<meta charset="utf-8">
<title>Lone Prairie Canvas &amp; Sound Jubilee — Festival Poster</title>
<link rel="stylesheet" href="https://fonts.googleapis.com/css2?family=Oswald:wght@300;400&family=Lato:wght@400;700;900&display=swap">
<style>
  :root {
    --ink: #111111;
    --paper: #ffffff;
    --accent: #f26522;
    --warm-skin: #a8553a;
  }
  * { box-sizing: border-box; margin: 0; padding: 0; }
  html, body { width: 1027px; height: 1200px; overflow: hidden; background: var(--paper); }
  .poster {
    position: relative; width: 1027px; height: 1200px;
    background: var(--paper); font-family: "Lato", sans-serif; color: var(--ink);
    overflow: hidden;
  }
  .photo-collage { position: absolute; left: 0; top: 0; width: 1027px; height: 500px; background: var(--ink); }
  .photo { position: absolute; }
  .photo--singer-top { left: 0; top: 0; width: 300px; height: 140px; background: linear-gradient(135deg, #9a9a9a, #3a3a3a); }
  .photo--guitarist { left: 0; top: 140px; width: 320px; height: 360px; background: linear-gradient(160deg, #4a4a4a, #0e0e0e); }
  .photo--vocalist { left: 300px; top: 0; width: 330px; height: 500px; background: radial-gradient(ellipse at 45% 30%, #c98a6a 0%, var(--warm-skin) 30%, #3a1c14 70%, #111 100%); }
  .photo--street { left: 630px; top: 0; width: 397px; height: 250px; background: linear-gradient(120deg, #5a5a5a, #1c1c1c 60%, #4a4a4a); }
  .photo--duo { left: 560px; top: 250px; width: 467px; height: 250px; background: linear-gradient(100deg, #8a8a8a, #2a2a2a 45%, #151515); }
  .wave { position: absolute; left: 0; top: 420px; width: 1027px; height: 130px; }

  .band { position: absolute; left: 20px; top: 640px; width: 1007px; height: 80px; background: var(--ink); }

  .festival-name {
    position: absolute; left: 40px; top: 648px; width: 300px; height: 64px;
    display: flex; align-items: center; gap: 12px;
    font-weight: 700; font-size: 20px; line-height: 1.2; color: var(--paper);
  }
  .festival-name .mark { flex: none; width: 30px; height: 30px; border-radius: 50%; background: var(--paper); }

  .headline { font-family: "Oswald", sans-serif; font-weight: 300; text-transform: uppercase; }
  .headline span { position: absolute; left: 380px; width: 580px; text-align: center; }
  .headline__top { top: 572px; font-size: 60px; line-height: 64px; }
  .headline__free { top: 640px; color: var(--accent); font-weight: 400; font-size: 78px; line-height: 80px; letter-spacing: 2px; }
  .headline__bottom { top: 722px; font-size: 60px; line-height: 64px; }

  .music-art { position: absolute; left: 800px; top: 800px; width: 227px; height: 300px; background: linear-gradient(200deg, #f2f2f2, #9a9a9a 60%, #2a2a2a); }

  .dates { position: absolute; left: 60px; top: 812px; font-family: "Oswald", sans-serif; font-weight: 300; font-size: 46px; line-height: 52px; text-transform: uppercase; }
  .dates__day { color: var(--accent); font-weight: 400; }
  .rule { position: absolute; left: 60px; top: 870px; width: 720px; height: 2px; background: var(--accent); }
  .admission { position: absolute; left: 60px; top: 880px; font-weight: 900; font-size: 22px; line-height: 30px; text-transform: uppercase; letter-spacing: .5px; }
  .admission__free { color: var(--accent); }

  .highlights { position: absolute; left: 60px; top: 950px; width: 720px; display: grid; grid-template-columns: 320px 1fr; column-gap: 20px; }
  .highlights ul { list-style: none; }
  .highlights li { position: relative; padding-left: 24px; font-weight: 700; font-size: 22px; line-height: 30px; }
  .highlights li::before { content: ""; position: absolute; left: 4px; top: 11px; width: 9px; height: 9px; border-radius: 50%; background: var(--accent); }

  .footer { position: absolute; left: 0; bottom: 0; width: 1027px; height: 90px; background: var(--ink); display: flex; align-items: center; justify-content: center; }
  .footer__url { color: var(--paper); font-weight: 900; font-size: 21px; letter-spacing: 3px; }
</style>
</head>
<body>
<main class="poster">
  <section class="photo-collage">
    <div class="photo photo--singer-top" role="img" aria-label="Black and white photo of a smiling performer"></div>
    <div class="photo photo--guitarist" role="img" aria-label="Black and white photo of a guitarist playing electric guitar"></div>
    <div class="photo photo--street" role="img" aria-label="Black and white photo of a historic downtown storefront"></div>
    <div class="photo photo--duo" role="img" aria-label="Photo of a rock duo in black jackets"></div>
    <div class="photo photo--vocalist" role="img" aria-label="Colour photo of a singer at a microphone"></div>
  </section>

  <svg class="wave" viewBox="0 0 1027 130" preserveAspectRatio="none" aria-hidden="true">
    <path d="M0 20 Q500 120 1027 10 L1027 130 L0 130 Z" fill="#111111"/>
    <path d="M0 50 Q500 135 1027 40 L1027 130 L0 130 Z" fill="#ffffff"/>
  </svg>

  <div class="band"></div>

  <h1 class="headline">
    <span class="headline__top">The event is</span>
    <span class="headline__free">Free</span>
    <span class="headline__bottom">to the public</span>
  </h1>

  <div class="festival-name"><span class="mark"></span><span>Lone Prairie Canvas &amp; Sound Jubilee</span></div>

  <div class="music-art" role="img" aria-label="Black and white illustration of a treble clef, microphone and speakers"></div>

  <p class="dates"><span class="dates__day">Friday,</span> October 14 – 16</p>
  <div class="rule"></div>
  <p class="admission"><span class="admission__free">Free admission</span> (VIP tickets available)</p>

  <div class="highlights">
    <ul>
      <li>Live music- 3 stages/<br>10 bands</li>
      <li>Film Screening</li>
    </ul>
    <ul>
      <li>Art vendors and art walk</li>
      <li>Live art murals</li>
      <li>Food trucks</li>
    </ul>
  </div>

  <footer class="footer"><span class="footer__url">www.loneprairiecanvasandsoundjubilee.example</span></footer>
</main>
</body>
</html>
```